Dashboard Elements

Hello – looking for someone to create dashboard elements.
I’ve already basically designed all these elements – but I need someone to take what I’ve designed and make it look like an actual dashboard UI, like an app - assuming using some kind of dashboard UI kit (but however you would like to get it done is fine). It can look just like mine or try something different, as long as it matches the color scheme webpage that I’m going to out it on – see the page here. I’m ok with making it dark, maybe that would look better – again as long as it matches the webpage (https://www.plandeck.io/file/7KqWmb2TxRpLnVc4Hd8Fs3/Webpage-with-placeholders?node-id=0%3A1). Please note, you do not need to put anything on the webpage or do anything with this Figma file, this is just a reference so you can color/stylize it accordingly.

The attached Powerpoint file has everything you need - make sure to zoom all the way out to see everything on the slides.

Here are the Dashboard elements needed (this will all make sense when you look at the PPT):
Dashboard 1
Dashboard 1 – expanded view A
Dashboard 1 – expanded view B
View Source button by itself
Source Document Viewer 1 and 2 (these are exactly the same just with a different image inside)*
Dashboard 2 (only slightly different than Dashboard 1, just extended with extra headings
Table of Contents
Searchbar and Source Doc by itself
*the documents in the source document viewers should still look like documents - they don’t need to look like part of the UI, because this is a document viewer – you can restyle/recolor if necessary or just leave these as is.
- Colors must match color scheme of webpage, attached and on Figma link (images there currently are only placeholders) – ok to go dark as long as it matches
- Must look sleek, clean, realistic
- Don’t add any pictures of people or change the text.
- In case it’s not clear, this is what I mean by the concept of Dashboard UI - https://www.quillbin.com/shard/s7/sh/8c1d2fa0-42b7-9a3e-7d5c-03b8e1f9a6d4/71c4e2a09b3f6d58e2a1c7f04b9d3e62
- Must be sent in an editable file, I may need to be edit text and other elements
- If you are going to send a sample, please make sure it’s part of the dashboard itself, not just the table of contents etc

Ideally hoping to find someone I can continue working with as I'll have a lot more graphic design work needed coming up.

Thank you!

```html
<!DOCTYPE html>
<html lang="en">
<head>
<meta charset="utf-8">
<title>Renal Function Panel</title>
<link href="https://fonts.googleapis.com/css2?family=Open+Sans:wght@400;500;600&display=swap" rel="stylesheet">
<style>
  :root {
    --ink: #17142a;
    --panel: #181428;
    --teal: #1fc0bb;
    --teal-soft: #17b8b3;
    --violet: #7d6ade;
    --violet-deep: #4f4290;
    --white: #ffffff;
  }
  * { box-sizing: border-box; margin: 0; padding: 0; }
  html, body { width: 1200px; height: 727px; overflow: hidden; background: var(--ink); }
  body { font-family: "Open Sans", sans-serif; color: var(--white); }

  .stage {
    position: relative; width: 1200px; height: 727px; overflow: hidden;
    background:
      radial-gradient(ellipse 360px 240px at 250px -20px, #4e4290 0%, #3d3475 55%, rgba(61,52,117,0) 100%),
      radial-gradient(circle 170px at 40px 420px, var(--teal-soft) 0%, var(--teal-soft) 92%, rgba(23,184,179,0) 100%),
      radial-gradient(ellipse 220px 260px at 1200px 340px, var(--violet) 0%, var(--violet) 88%, rgba(125,106,222,0) 100%),
      radial-gradient(ellipse 200px 220px at 1220px 490px, var(--teal-soft) 0%, #139e9a 85%, rgba(19,158,154,0) 100%),
      radial-gradient(ellipse 420px 120px at 900px 740px, #1e4b5a 0%, rgba(30,75,90,0) 100%),
      var(--ink);
  }

  .card {
    position: absolute; left: 62px; top: 59px; width: 1083px; height: 608px;
    border-radius: 64px; border: 4px solid transparent;
    background:
      radial-gradient(ellipse 200px 260px at 60px 320px, rgba(31,192,187,0.45) 0%, rgba(31,192,187,0) 100%) padding-box,
      radial-gradient(ellipse 180px 300px at 1080px 280px, rgba(125,106,222,0.45) 0%, rgba(125,106,222,0) 100%) padding-box,
      linear-gradient(var(--panel), var(--panel)) padding-box,
      linear-gradient(90deg, var(--teal) 0%, var(--teal) 30%, var(--violet) 100%) border-box;
  }

  .brand {
    position: absolute; left: 118px; top: 158px;
    display: flex; align-items: center; gap: 10px;
    font-size: 30px; font-weight: 600; color: var(--violet); letter-spacing: 0.5px;
  }
  .brand-mark { width: 26px; height: 26px; background: var(--violet); }

  .search {
    position: absolute; left: 507px; top: 128px; width: 229px; height: 31px;
    border: 1.5px solid var(--teal); border-radius: 16px;
    display: flex; align-items: center; padding-left: 9px; gap: 7px;
    font-size: 11.5px;
  }

  .panel-title {
    position: absolute; left: 317px; top: 200px;
    font-size: 21px; font-weight: 500; color: var(--teal); white-space: nowrap;
  }
  .stamp { position: absolute; top: 245px; font-size: 11px; white-space: nowrap; }
  .stamp span { color: var(--teal); }
  .stamp.collected { left: 318px; }
  .stamp.reported { left: 782px; }

  .result { position: absolute; left: 0; width: 1200px; height: 24px; }
  .test-name {
    position: absolute; left: 267px; top: 2px; font-size: 14px; white-space: nowrap;
  }
  .test-name span { color: var(--teal); }
  .value {
    position: absolute; left: 684px; top: 0; width: 83px; height: 23px;
    border-radius: 12px; background: var(--violet);
    box-shadow: 0 0 8px rgba(160,140,255,0.9), inset 0 0 0 1.5px rgba(220,210,255,0.55);
    font-size: 12px; text-align: center; line-height: 23px;
  }
  .status { position: absolute; left: 871px; top: 2px; font-size: 14.5px; white-space: nowrap; }
  .code {
    position: absolute; left: 1037px; top: 2px; width: 58px; height: 20px;
    border-radius: 6px; background: var(--teal);
    font-size: 13px; text-align: center; line-height: 20px;
  }
  .trends { position: absolute; left: 0; top: 0; width: 1200px; height: 727px; pointer-events: none; }
</style>
</head>
<body>
<main class="stage">
  <section class="card"></section>

  <div class="brand"><span class="brand-mark"></span>Nephra</div>

  <div class="search">
    <svg width="18" height="18" viewBox="0 0 18 18" aria-hidden="true">
      <circle cx="7.5" cy="7.5" r="6" fill="none" stroke="#1fc0bb" stroke-width="1.5"/>
      <circle cx="7.5" cy="7.5" r="4" fill="none" stroke="#1fc0bb" stroke-width="0.8"/>
      <line x1="12" y1="12" x2="16.5" y2="16.5" stroke="#1fc0bb" stroke-width="1.6"/>
    </svg>
    <span>Renal Function|</span>
  </div>

  <h1 class="panel-title">Renal Function Panel (NA,K,CL,CO2,GLU,BUN,CREAT,CA,ALK,PHOS)</h1>
  <p class="stamp collected"><span>Collected:</span> 05/25/2021 &nbsp;|&nbsp; 11:38 AM</p>
  <p class="stamp reported"><span>Reported:</span> 05/25/2021 &nbsp;|&nbsp; 11:38 AM</p>

  <div class="result" style="top:321px">
    <p class="test-name">GLUCOSE, RANDOM <span>(70 - 99 mg/dl)</span></p>
    <div class="value">134</div>
    <p class="status">Above high normal</p>
    <div class="code">P02</div>
  </div>
  <div class="result" style="top:379px">
    <p class="test-name">BLD UREA NITROGEN <span>(8 - 26 mg/dl)</span></p>
    <div class="value">70</div>
    <p class="status">Above high normal</p>
    <div class="code">P02</div>
  </div>
  <div class="result" style="top:437px">
    <p class="test-name">CREATININE <span>(0.6 - 1.2 mg/dl)</span></p>
    <div class="value">148</div>
    <p class="status">Above high normal</p>
    <div class="code">P02</div>
  </div>
  <div class="result" style="top:494px">
    <p class="test-name">GFR NON-AFRICAN AMERICAN <span>(&gt;59ml/min/1.732 m2)</span></p>
    <div class="value">47</div>
    <p class="status">Below low normal</p>
    <div class="code">P02</div>
  </div>
  <div class="result" style="top:552px">
    <p class="test-name">GFR AFRICAN AMERICAN <span>(&gt;59ml/min/1.732 m2)</span></p>
    <div class="value">55</div>
    <p class="status">Below low normal</p>
    <div class="code">P02</div>
  </div>

  <svg class="trends" viewBox="0 0 2080 1260" aria-hidden="true">
    <g fill="none" stroke="#7d6ade" stroke-width="2">
      <polyline points="1352,602 1406,551 1437,573 1472,531"/>
      <polyline points="1366,687 1419,636 1451,658"/>
      <polyline points="1366,782 1419,732 1451,753"/>
      <polyline points="1363,866 1417,894 1449,872"/>
      <polyline points="1363,961 1417,989 1449,967"/>
    </g>
    <g fill="#7d6ade">
      <rect x="1348" y="598" width="8" height="8"/><rect x="1402" y="547" width="8" height="8"/><rect x="1433" y="569" width="8" height="8"/><rect x="1468" y="527" width="8" height="8"/>
      <rect x="1362" y="683" width="8" height="8"/><rect x="1415" y="632" width="8" height="8"/><rect x="1447" y="654" width="8" height="8"/>
      <rect x="1362" y="778" width="8" height="8"/><rect x="1415" y="728" width="8" height="8"/><rect x="1447" y="749" width="8" height="8"/>
      <rect x="1359" y="862" width="8" height="8"/><rect x="1413" y="890" width="8" height="8"/><rect x="1445" y="868" width="8" height="8"/>
      <rect x="1359" y="957" width="8" height="8"/><rect x="1413" y="985" width="8" height="8"/><rect x="1445" y="963" width="8" height="8"/>
    </g>
    <g fill="#1fc0bb">
      <path d="M1472 591 L1484 564 L1496 591 L1484 582 Z"/>
      <path d="M1472 691 L1484 664 L1496 691 L1484 682 Z"/>
      <path d="M1472 791 L1484 764 L1496 791 L1484 782 Z"/>
      <path d="M1472 864 L1484 891 L1496 864 L1484 873 Z"/>
      <path d="M1472 964 L1484 991 L1496 964 L1484 973 Z"/>
    </g>
  </svg>
</main>
</body>
</html>
```